Business Card Design

Timberline Cabinetry in Colorado. We recently changed our logo the use the colors grey and blue. Our company motto is "where ideas come to life" Wanting a business card to pop and stand out. I attached our new logo and colors scheme

Industry/Entity Type

Business

```html
<!DOCTYPE html>
<html lang="en">
<head>
<meta charset="utf-8">
<title>Timberline Cabinetry – Business Card</title>
<link rel="stylesheet" href="https://fonts.googleapis.com/css2?family=Oswald:wght@700&family=Parisienne&display=swap">
<style>
  :root {
    --panel: #2f2f2f;
    --band: #34506e;
    --ink: #ffffff;
    --tagline: #f2f2f2;
    --wall: #ececec;
    --cabinet: #7d7f82;
    --floor: #c8ad88;
  }
  html, body {
    margin: 0;
    padding: 0;
    width: 1200px;
    height: 703px;
    overflow: hidden;
    background: var(--panel);
  }
  .card {
    position: relative;
    width: 1200px;
    height: 703px;
    background: var(--panel);
    overflow: hidden;
  }
  .kitchen-photo {
    position: absolute;
    left: 0;
    top: 0;
    width: 773px;
    height: 557px;
    background: linear-gradient(180deg, var(--wall) 0%, #d9d9d9 18%, var(--cabinet) 45%, #6f7073 68%, #b59c7a 84%, var(--floor) 100%);
  }
  .tagline-band {
    position: absolute;
    left: 0;
    top: 557px;
    width: 773px;
    height: 146px;
    background: var(--band);
  }
  .tagline {
    position: absolute;
    left: 125px;
    top: 578px;
    margin: 0;
    font-family: "Parisienne", cursive;
    font-size: 58px;
    font-weight: 400;
    color: var(--tagline);
    white-space: nowrap;
  }
  .brand {
    position: absolute;
    right: 62px;
    top: 280px;
    margin: 0;
    text-align: right;
    font-family: "Oswald", sans-serif;
    font-weight: 700;
    color: var(--ink);
    text-transform: uppercase;
    line-height: 1.05;
  }
  .brand-name {
    display: block;
    font-size: 64px;
  }
  .brand-sub {
    display: block;
    font-size: 38px;
    margin-top: 2px;
  }
  .contact {
    position: absolute;
    right: 62px;
    top: 445px;
    margin: 0;
    padding: 0;
    list-style: none;
    text-align: right;
    font-family: "Oswald", sans-serif;
    font-weight: 700;
    font-size: 25px;
    color: var(--ink);
    line-height: 50px;
  }
</style>
</head>
<body>
  <main class="card">
    <div class="kitchen-photo" role="img" aria-label="Photo of a modern kitchen with grey cabinets, light wood trim, a wall oven and a wooden floor"></div>
    <div class="tagline-band"></div>
    <p class="tagline">where ideas come to life</p>

    <h1 class="brand">
      <span class="brand-name">Timberline</span>
      <span class="brand-sub">Cabinetry Co.</span>
    </h1>

    <ul class="contact">
      <li>timberline cabinetry</li>
      <li>303-555-0142</li>
      <li>hello@timberlinecabinetry.com</li>
      <li>timberlinecabinetry.com</li>
    </ul>
  </main>
</body>
</html>
```